Combining web page

We need a PSD webpage design for our PrestaShop store that shows food combining rules, you can see an example that we put here, you can follow the same information and food image combinations. You are just doing the design but the images when implemented on the website will be clickable that goes to product categories, all text and images will be editable.

This is just an example:
http://velmoraharvest.com/content/7-food-combining-rules

Target Market(s)

Natural Product and supplement industry

Industry/Entity Type

Store

Number of Pages Required

1 page

Colors

Designer to choose colors to be used in the design.

Requirements
Must have
• 1. Clear images.
• 2. Clear readable text.
• 3. Company name shown Velmora Harvest.
• 4. Follow the food rules as seen on the web page example, but not the same design.
• 5. Logo should be seen.
• 7. All text and images will be editable.
• 8. Make sure the food images are in their proper groups.
• 9. You are not coping the design we gave you but the details have to be the same, copy the text and the image food groups are important, you cannot just put any food in a group, and the combinations are important.
Nice to have
• Here is the website it is for http://velmoraharvest.com/

```html
<!DOCTYPE html>
<html lang="en">
<head>
<meta charset="utf-8">
<title>Velmora Harvest – Food Combining Rules</title>
<link href="https://fonts.googleapis.com/css2?family=Open+Sans:ital,wght@0,400;0,600;0,700;0,800;1,700&family=PT+Serif&display=swap" rel="stylesheet">
<style>
:root{
  --backdrop:#0c0e0b;
  --page:#ffffff;
  --green:#3cb80e;
  --green-dark:#2f9a0a;
  --red:#e3153a;
  --ink:#222;
  --muted:#555;
  --row-peach:#fbe8da;
  --row-cream:#fbf8e4;
  --row-pink:#fbe0ee;
  --key-bg:#e6fbb6;
  --col-citrus:#f6c09a;
  --col-fruit:#f3dcc2;
  --col-sweet:#f7eaa5;
  --col-nut:#f1ecd0;
  --col-grain:#d9dfa0;
  --col-legume:#eef0d8;
  --col-melon:#f39ccc;
  --col-succ:#f6d2e2;
  --col-veg:#e0d596;
  --footer:#141613;
}
*{box-sizing:border-box;margin:0;padding:0}
html,body{width:1200px;height:1200px;overflow:hidden;background:var(--backdrop);font-family:"Open Sans",sans-serif;color:var(--ink)}
.canvas{position:relative;width:1200px;height:1200px}
.page{position:absolute;left:406px;top:77px;width:381px;height:883px;background:var(--page);overflow:hidden}
.abs{position:absolute}
.produce-corner{position:absolute}
.search{left:16px;top:11px;width:80px;height:10px;border-bottom:1px solid #bbb;font-size:5px;font-style:italic;font-weight:700;line-height:10px;z-index:2}
.search svg{position:absolute;right:0;top:1px}
.brand{left:115px;top:9px;width:150px;display:flex;align-items:center;justify-content:center;gap:4px;white-space:nowrap;z-index:2}
.brand-mark{width:9px;height:9px;background:var(--red);border-radius:50%;flex:none}
.brand-name{font-family:"PT Serif",serif;font-size:14px;color:var(--green);line-height:1}
.brand-tag{left:115px;top:28px;width:150px;text-align:center;font-size:4px;color:var(--muted);white-space:nowrap;z-index:2}
.account{right:16px;top:9px;font-size:5px;text-align:right;line-height:7px;z-index:2}
.nav{left:0;top:48px;width:381px;display:flex;justify-content:space-around;font-size:7px;color:#333;padding:0 10px;white-space:nowrap;z-index:2}
.hero-img{left:80px;top:80px;width:115px;height:88px;border-radius:10px;background:linear-gradient(90deg,#f07a2a,#4cab2a 50%,#d8263a)}
.hero-lead{left:200px;top:101px;font-size:6.5px;color:var(--green);font-weight:600}
.hero-big{left:205px;top:105px;font-size:38px;font-style:italic;color:var(--red);font-family:"PT Serif",serif;line-height:1}
.hero-sub{left:200px;top:146px;width:115px;text-align:right;font-size:6px;color:var(--green);font-weight:700;line-height:9px}
.arrow{top:119px;color:var(--green);font-size:14px;z-index:2}
.welcome{left:0;top:180px;width:381px;text-align:center;font-family:"PT Serif",serif;font-weight:400;font-size:17px;color:var(--green)}
.welcome-text{left:14px;top:206px;width:353px;text-align:center;font-size:5px;line-height:8px;font-weight:600}
.band{left:6px;top:238px;width:370px;height:36px;background:var(--green);text-align:center;color:#fff}
.band h1{font-family:"PT Serif",serif;font-weight:400;font-size:17px;line-height:24px}
.band .sub{display:flex;justify-content:space-around;font-size:6.5px;font-style:italic;font-weight:700;padding:0 90px}
.intro{left:11px;top:286px;width:262px;font-size:5px;line-height:8px;font-weight:600}
.intro h3{font-size:6.5px;font-style:italic;color:var(--green);margin-bottom:3px}
.intro p{margin-bottom:3px}
.runner{left:282px;top:291px;width:98px;height:104px;background:var(--green);border-radius:40% 30% 45% 35%}
.easy{left:11px;top:390px;font-size:14px;font-weight:800;color:var(--green)}
.easy-sub{left:11px;top:410px;font-size:6.5px;font-weight:600;color:#333}
.chart{left:8px;top:427px;width:367px}
.grid{display:grid;grid-template-columns:143px repeat(9,1fr)}
.key{height:25px;background:var(--key-bg);font-size:4px;font-weight:700}
.key .legend{display:flex;gap:22px;padding:8px 6px;line-height:5px}
.key .head{display:flex;align-items:center;justify-content:center;text-align:center;font-size:3.6px;line-height:4px;padding:1px}
.c1{background:var(--col-citrus)}.c2{background:var(--col-fruit)}.c3{background:var(--col-sweet)}.c4{background:var(--col-nut)}.c5{background:var(--col-grain)}.c6{background:var(--col-legume)}.c7{background:var(--col-melon)}.c8{background:var(--col-succ)}.c9{background:var(--col-veg)}
.row{margin-top:4px;height:36px}
.row.peach{background:var(--row-peach)}.row.cream{background:var(--row-cream)}.row.pink{background:var(--row-pink)}
.group{position:relative;padding-left:52px;padding-top:4px;overflow:hidden}
.group .num{position:absolute;left:3px;top:3px;font-size:6px;font-weight:700}
.group .photo{position:absolute;left:10px;top:6px;width:38px;height:26px;border-radius:40%}
.group .name{font-size:5.5px;font-weight:600;color:#333;white-space:nowrap}
.group .items{font-size:3px;line-height:4px;color:#444;margin-top:2px;max-width:86px}
.cell{display:flex;align-items:center;justify-content:center;font-size:7px;font-weight:600;color:#444;border-left:1px dashed #b9c9a0;white-space:nowrap}
.principle{left:0;top:809px;width:381px;text-align:center;font-size:12px;font-weight:800;color:var(--green)}
.rule{left:14px;top:828px;width:353px;border-top:1px solid #ccc}
.principle-cols{left:16px;top:835px;width:350px;display:grid;grid-template-columns:repeat(4,1fr);gap:6px;font-size:3.2px;line-height:4.4px}
.footer{position:absolute;left:406px;top:960px;width:381px;height:140px;background:var(--footer);text-align:center;color:#fff}
.socials{position:absolute;left:170px;top:22px;display:flex;gap:4px}
.socials span{width:12px;height:12px;background:#4a7bd0;border-radius:2px}
.socials span:last-child{background:#c23c7c}
.signup{position:absolute;left:81px;top:45px;display:flex}
.signup .field{width:135px;height:23px;background:#fff;border:1px solid #ccc}
.signup .btn{width:83px;height:23px;background:var(--green);font-size:10px;line-height:23px}
.notice{position:absolute;left:0;top:76px;width:381px;font-size:5px;line-height:7px;color:var(--green)}
.links{position:absolute;left:0;top:102px;width:381px;font-size:8px;line-height:13px;white-space:nowrap}
</style>
</head>
<body>
<div class="canvas">
  <main class="page">
    <div class="produce-corner" role="img" aria-label="Fresh fruits and vegetables framing the top left" style="left:0;top:0;width:60px;height:190px;background:linear-gradient(160deg,#f4d36a,#b7d77c 55%,rgba(255,255,255,0))"></div>
    <div class="produce-corner" role="img" aria-label="Fresh fruits and vegetables framing the top right" style="right:0;top:0;width:60px;height:190px;background:linear-gradient(200deg,#f0b34a,#a9d072 55%,rgba(255,255,255,0))"></div>
    <div class="produce-corner" role="img" aria-label="Fresh produce along the top edge" style="left:60px;top:0;width:261px;height:12px;background:linear-gradient(90deg,#e8efd0,#f6e2c0,#e8efd0)"></div>

    <div class="abs search">Search Here
      <svg width="7" height="7" viewBox="0 0 10 10"><circle cx="4" cy="4" r="3" fill="none" stroke="#333"/><line x1="6" y1="6" x2="9" y2="9" stroke="#333"/></svg>
    </div>
    <div class="abs brand"><span class="brand-mark"></span><span class="brand-name">Velmora Harvest</span></div>
    <div class="abs brand-tag">Wholesome foods for today's kitchen</div>
    <div class="abs account">Log In<br>(0 Cart)</div>

    <nav class="abs nav"><span>Home</span><span>Food Combining Rules</span><span>Our Products</span><span>Ingredients</span><span>Health Concerns</span></nav>

    <span class="abs arrow" style="left:45px">&#8249;</span>
    <div class="abs hero-img" role="img" aria-label="Glasses of fresh orange, green and red juice with vegetables"></div>
    <div class="abs hero-lead">Organic &amp; healthy food</div>
    <div class="abs hero-big">100%</div>
    <div class="abs hero-sub">Fresh Fruits, Vegetable &amp;<br>juice Available here</div>
    <span class="abs arrow" style="left:330px">&#8250;</span>

    <h2 class="abs welcome">Welcome To&nbsp; Velmora Foods</h2>
    <p class="abs welcome-text">Our kitchen begins with whole foods grown simply and prepared with care. We gather grains, fruits, nuts and vegetables from trusted farms and bring them to your table so every meal can nourish the body, lift the spirit and honour the old ways of eating well.</p>

    <div class="abs band">
      <h1>Food Combining Rules</h1>
      <div class="sub"><span>NINE HARVESTS</span><span>A good cook chart</span></div>
    </div>

    <div class="abs intro">
      <h3>GRAINS, FRUITS, NUTS AND VEGETABLE</h3>
      <p>constitute the diet chosen for us by our creator. this food prepared in as simple and natural a manner as possible, are the most healthful and nourishing. They impart a strength, a power of endurance, and vigor of intellect, that are not afforded by a more complex &amp; stimulating diet. In Grains, fruits, vegetable &amp; nuts are to be found all the food elements that we need. E.R. Marlowe Diet &amp; foods, Pg.363</p>
      <p>The liability to take disease is increased tenfold by meat eating. It is a mistake to suppose that muscular strength depend on the use of animal food. The needs of the system can be better supply and more vigorous health can be enjoyed without its use. The Grains with fruits, nuts &amp; vegetable contain all the nutritive properties necessary to make good blood. when flesh food is discarded its place should be supplied with the varities of Grains nuts, vegetable &amp; fruits that will be both nurishing &amp; appetizing. E.R. Marlowe Diet &amp; foods, Pg.386, 396,315.</p>
    </div>
    <div class="abs runner" role="img" aria-label="Green silhouette of a runner in motion"></div>

    <h2 class="abs easy">FOOD COMBINING MADE EASY</h2>
    <div class="abs easy-sub">natural foods FOOD GROUPS - CLASSIFIED</div>

    <section class="abs chart">
      <div class="grid key">
        <div class="legend"><span>Key : XX Combines Well<br>X Fair Compatibility</span><span>NR Not Recommended<br>No Not Compatible</span></div>
        <div class="head c1">CITRUS ACID FRUITS</div><div class="head c2">FRUITS (SUB- ACID)</div><div class="head c3">SWEET FRUITS (PALM FRUITS)</div><div class="head c4">NUTRAL FRUITS RAW NUTS SEEDS</div><div class="head c5">GRAINS</div><div class="head c6">LEGUMES DRY SPROUTS</div><div class="head c7">MELONS</div><div class="head c8">SUCCULENT FRUITS TOMATOES</div><div class="head c9">VEGETABLES</div>
      </div>

      <div class="grid row peach">
        <div class="group"><span class="num">1.</span><div class="photo" role="img" aria-label="Lemons and limes" style="background:#d8e04a"></div><div class="name">CITRUS - ACID FRUITS</div><div class="items">orange lime lemon grapefruit kiwi pineapple tangerine sour plum</div></div>
        <div class="cell">XX</div><div class="cell">XX</div><div class="cell">X</div><div class="cell">XX</div><div class="cell">NR</div><div class="cell">X- NR</div><div class="cell">X</div><div class="cell">NO</div><div class="cell">NO</div>
      </div>
      <div class="grid row cream">
        <div class="group"><span class="num">2.</span><div class="photo" role="img" aria-label="Mixed fruits with bananas, apples and grapes" style="background:#e4a23a"></div><div class="name">FRUITS &nbsp;(SUB- ACID)</div><div class="items">apple pear peach apricot cherry grape mango papaya berries banana</div></div>
        <div class="cell">XX</div><div class="cell">XX</div><div class="cell">XX</div><div class="cell">XX</div><div class="cell">XX</div><div class="cell">X- NR</div><div class="cell">X</div><div class="cell">NO</div><div class="cell">NO</div>
      </div>
      <div class="grid row cream" style="height:34px">
        <div class="group"><span class="num">3.</span><div class="photo" role="img" aria-label="Dates, figs and sweet dried fruits" style="background:#c9842f"></div><div class="name">SWEET FRUITS (PALM FRUITS)</div><div class="items">dates figs raisins prunes dried apricot persimmon sweet grapes</div></div>
        <div class="cell">X</div><div class="cell">XX</div><div class="cell">XX</div><div class="cell">XX</div><div class="cell">XX</div><div class="cell">NO</div><div class="cell">X- NR</div><div class="cell"></div><div class="cell">NO</div>
      </div>
      <div class="grid row cream" style="height:31px">
        <div class="group"><span class="num">4.</span><div class="photo" role="img" aria-label="Raw nuts and seeds" style="background:#b07a4a"></div><div class="name">NUTRAL FRUITS RAW NUTS SEEDS</div><div class="items">almond walnut cashew pecan sunflower pumpkin sesame avocado</div></div>
        <div class="cell">XX</div><div class="cell">XX</div><div class="cell">XX</div><div class="cell">XX</div><div class="cell">XX</div><div class="cell">XX</div><div class="cell">X</div><div class="cell">XX</div><div class="cell">XX</div>
      </div>
      <div class="grid row pink" style="height:31px">
        <div class="group"><span class="num">5.</span><div class="photo" role="img" aria-label="Bowls of whole grains" style="background:#c8955a"></div><div class="name">GRAINS</div><div class="items">barley millet oats rice rye wheat corn quinoa buckwheat</div></div>
        <div class="cell">NR</div><div class="cell">XX</div><div class="cell">XX</div><div class="cell">XX</div><div class="cell">XX</div><div class="cell">XX</div><div class="cell">X- NR</div><div class="cell">XX</div><div class="cell">XX</div>
      </div>
      <div class="grid row cream">
        <div class="group"><span class="num">6.</span><div class="photo" role="img" aria-label="Dry legumes and fresh sprouts" style="background:#c9c79a"></div><div class="name">LEGUMES DRY SPROUTS</div><div class="items">lentils chickpeas beans split peas soy mung sprouts alfalfa</div></div>
        <div class="cell">X- NR</div><div class="cell">X- NR</div><div class="cell">NO</div><div class="cell">XX</div><div class="cell">XX</div><div class="cell">XX</div><div class="cell">NR</div><div class="cell">XX</div><div class="cell">XX</div>
      </div>
      <div class="grid row peach" style="height:37px">
        <div class="group"><span class="num">7.</span><div class="photo" role="img" aria-label="Sliced melons" style="background:#ef9a5a"></div><div class="name">MELONS</div><div class="items">watermelon cantaloupe honeydew casaba musk melon</div></div>
        <div class="cell">X</div><div class="cell">X</div><div class="cell">X- NR</div><div class="cell">X</div><div class="cell">X- NR</div><div class="cell">NR</div><div class="cell">XX</div><div class="cell">NR</div><div class="cell">NO</div>
      </div>
      <div class="grid row pink">
        <div class="group"><span class="num">8.</span><div class="photo" role="img" aria-label="Tomatoes, peppers and succulent fruits" style="background:#d9463e"></div><div class="name">SUCCULENT FRUITS- TOMATOES</div><div class="items">tomato cucumber zucchini bell pepper eggplant squash okra</div></div>
        <div class="cell">NO</div><div class="cell">NO</div><div class="cell">NO</div><div class="cell">XX</div><div class="cell">XX</div><div class="cell">XX</div><div class="cell">NR</div><div class="cell">XX</div><div class="cell">XX</div>
      </div>
      <div class="grid row cream" style="height:33px">
        <div class="group"><span class="num">9.</span><div class="photo" role="img" aria-label="Assorted fresh vegetables" style="background:#6fae3a"></div><div class="name">VEGETABLES</div><div class="items">carrot beet kale spinach lettuce celery broccoli onion potato</div></div>
        <div class="cell">NO</div><div class="cell">NO</div><div class="cell">NO</div><div class="cell">XX</div><div class="cell">XX</div><div class="cell">XX</div><div class="cell">NO</div><div class="cell">XX</div><div class="cell">XX</div>
      </div>
    </section>

    <h2 class="abs principle">PRINCIPLE OF EATING</h2>
    <div class="abs rule"></div>
    <div class="abs principle-cols">
      <p>Eat slowly and chew each mouthful well so the body can draw the most from every food. Keep meals simple, with few dishes at one sitting, and leave space between meals for rest.</p>
      <p>Take fruit and vegetables at separate meals where you can. Drink water between meals rather than with them, and let the last meal of the day be light and early.</p>
      <p>Choose foods in season and close to their natural state. Favour whole grains, fresh fruit, greens and nuts, and keep sugar, salt and rich sauces to a gentle minimum.</p>
      <p>Regular hours, fresh air, sunlight and daily exercise help the body use its food well. A calm and thankful mind at the table is part of good digestion too.</p>
    </div>
  </main>

  <footer class="footer">
    <div class="socials" aria-label="Social links"><span></span><span></span><span></span></div>
    <div class="signup"><div class="field"></div><div class="btn">SUBSCRIBE</div></div>
    <p class="notice">You may unsubscribe at any moment. For that purpose<br>please find our contact info in the legal notice.</p>
    <p class="links">Delivery | Legal Notice | Terms and conditions | About us |Secure payment<br>Food Combining | Rules TRELL COMBINING Trell CSS CODE | Contact us | Sitemap Stores</p>
  </footer>
</div>
</body>
</html>
```